Flyer-Design für Immobilienmakler & Bauträger
Zielgruppe
Wir sind Immobilienmakler & Bauträger
Zielgruppe sind alle, die eine Immobile besitzen und (jetzt oder später) verkaufen möchten
Wir möchten vermehrt Werbung in den lokalen Ortszeitungen machen um bekannter zu werden!
Bei der Vielzahl von Maklern möchten wir hervorstechen und uns auch von den ganzen Franchise Unternhemen abheben
Als kleines Familienunternhemen steht bei uns neben einer erfolgreichen Vermarktung Zuverlässigkeit, Fairness und Freundlichkeit an oberster Stelle!
WOVA (WOhnraum VAldorf) besteht aus
Reinhold Valdorf (Geschäftsführer)
Svenja Valdorf (Tochter)
Jonas Valdorf (Sohn)
Aufgabenstellung
Heidelberg und die Umgebung soll uns als freundliches, zuverlässiges & erfolgreiches Maklerteam kennenlernen, hierfür benötigen wir einen Flyer mit Vorder- und Rückseite
Die Vorderseite soll übersichtlich sein und auf den ersten Blick erkennen lassen
- wer wir sind (gerne auch mit Bildern von uns - diese sollen später von uns durch aktuelle ersetzt werden können)
- was wir suchen (zum Verkauf stehende Objekte - sowohl zur Vermarktung als auch zum Eigenankauf)
- was wir können - bzw was wir tun - Immobilien erfolgreich vermitteln/vermarkeln - für Auftraggeber kostenfrei!!
Gerne auch mit
'Ihr freundliches Immobilienbüro im Herzen von Neuenheim'
Wir haben ebenfalls eine Bauträgergesellschaft, vll könnte man auch dieses Logo mit einfließen lassen
TKR GmbH
Auf der Rückseite soll das Thema Tippgeber aufgegriffen werden -
Ihr Wissen ist bares Geld wert
oder
Wir belohnen Ihr Wissen
Ihre Freunde, Bekannte, Verwandte, Nachbarn oder Vermieter haben Ihnen von Verkaufsplänen ihrer Immobilie erzählt?
Geben Sie den Tipp an uns weiter! Führt dieser zum Verkauf der benannten Immobilie durch uns, ist uns das 10% unserer Maklerprovision (netto) wert.
Und so geht’s:
1. Sie melden sich per E-Mail, Telefon oder über das Homepage-Formular und benennen den Eigentümer und das Objekt, welches verkauft werden soll. Teilen Sie in diesem Rahmen auch mit, ob Ihr Tipp anonym behandelt werden soll.
2. Wir setzen uns mit dem Eigentümer in Verbindung
3. Sie erhalten von uns eine Information
4. Nach erfolgreichen Verkauf erhalten Sie Ihre Tippgeberprovision gutgeschrieben.
Die Tippgebervergütungen werden nach Abschluss der Verträge und nach Eingang der Maklerprovision innerhalb von 7 Tagen ausbezahlt. Bei unterlassener Zahlung der Maklerprovision an uns kann auch keine Auszahlung der Tippgeberprovision erfolgen. Bei mehreren Tipps zu ..

```html
<!DOCTYPE html>
<html lang="de">
<head>
<meta charset="utf-8">
<title>Tippgeber – Ihr Wissen ist bares Geld wert</title>
<link rel="stylesheet" href="https://fonts.googleapis.com/css2?family=Mulish:wght@600;700;800&display=swap">
<style>
  :root {
    --green: #27b33f;
    --ink: #111111;
    --paper: #ffffff;
  }
  html, body {
    margin: 0;
    padding: 0;
    overflow: hidden;
    background: var(--paper);
  }
  .flyer {
    position: relative;
    width: 848px;
    height: 1200px;
    background: var(--paper);
    font-family: "Mulish", "Century Gothic", sans-serif;
    color: var(--ink);
    overflow: hidden;
  }
  .headline {
    position: absolute;
    left: 52px;
    top: 38px;
    margin: 0;
    font-size: 52px;
    font-weight: 800;
    letter-spacing: 0.2px;
    color: var(--green);
    line-height: 1;
  }
  .question {
    position: absolute;
    left: 52px;
    top: 116px;
    margin: 0;
    font-size: 21px;
    font-weight: 800;
    line-height: 26px;
  }
  .intro {
    position: absolute;
    left: 52px;
    top: 184px;
    width: 740px;
    margin: 0;
    font-size: 16.4px;
    font-weight: 700;
    line-height: 21px;
  }
  .steps-title {
    position: absolute;
    left: 52px;
    top: 318px;
    margin: 0;
    font-size: 21px;
    font-weight: 700;
    color: var(--green);
  }
  .step-icon {
    position: absolute;
    fill: var(--green);
  }
  .step-text {
    position: absolute;
    left: 152px;
    margin: 0;
    font-size: 16.4px;
    font-weight: 700;
    line-height: 21px;
    width: 660px;
  }
  .icon-glyph {
    position: absolute;
    color: var(--green);
    font-weight: 800;
    line-height: 1;
  }
  .fineprint {
    position: absolute;
    left: 152px;
    top: 671px;
    width: 660px;
    margin: 0;
    font-size: 12.4px;
    font-weight: 700;
    line-height: 15.6px;
  }
  .website {
    position: absolute;
    right: 45px;
    top: 1130px;
    margin: 0;
    font-size: 16.4px;
    font-weight: 700;
  }
</style>
</head>
<body>
<main class="flyer">
  <h1 class="headline">Ihr Wissen ist bares Geld wert</h1>

  <h2 class="question">Ihre Freunde, Bekannte, Verwandte, Nachbarn oder Vermieter<br>haben Ihnen von Verkaufsplänen ihrer Immobilie erzählt?</h2>

  <p class="intro">Geben Sie den Tipp an uns weiter! Führt dieser zum Verkauf der benannten Immobilie durch uns, ist uns das 10% unserer Maklerprovision (netto) wert.</p>

  <h3 class="steps-title">Und so geht’s:</h3>

  <!-- Step 1: contact -->
  <svg class="step-icon" style="left:53px;top:373px" width="42" height="26" viewBox="0 0 42 26" aria-hidden="true">
    <rect x="0" y="0" width="42" height="26"/>
    <polyline points="1,1 21,14 41,1" fill="none" stroke="#ffffff" stroke-width="1.6"/>
  </svg>
  <svg class="step-icon" style="left:100px;top:372px" width="36" height="28" viewBox="0 0 36 28" aria-hidden="true">
    <path d="M4 1 L9 0 L12 8 L9 11 C12 17 17 21 23 23 L26 20 L34 22 L35 26 C33 28 28 28 22 26 C12 22 5 15 2 8 C1 5 2 2 4 1 Z"/>
  </svg>
  <p class="step-text" style="top:354px">Sie melden sich per E-Mail, Telefon oder über das Homepage-Formular und benennen den Eigentümer und das Objekt, welches verkauft werden soll. Teilen Sie in diesem Rahmen auch mit, ob Ihr Tipp anonym behandelt werden soll.</p>

  <!-- Step 2: owner -->
  <svg class="step-icon" style="left:53px;top:435px" width="42" height="34" viewBox="0 0 42 34" aria-hidden="true">
    <path d="M0 9 L21 0 L42 9 L42 34 L24 34 L24 27 L18 27 L18 34 L0 34 Z"/>
  </svg>
  <p class="step-text" style="top:449px">Wir setzen uns mit dem Eigentümer in Verbindung.</p>

  <!-- Step 3: information -->
  <span class="icon-glyph" style="left:51px;top:487px;font-size:46px" aria-hidden="true">@</span>
  <p class="step-text" style="top:499px">Sie erhalten von uns eine Information.</p>

  <!-- Step 4: payout -->
  <span class="icon-glyph" style="left:52px;top:547px;font-size:40px" aria-hidden="true">€</span>
  <p class="step-text" style="top:556px">Nach erfolgreichen Verkauf erhalten Sie Ihre Tippgeberprovision gutgeschrieben.</p>

  <p class="fineprint">Die Tippgebervergütungen werden nach Abschluss der Verträge und nach Eingang der Maklerprovision innerhalb von 7 Tagen ausbezahlt. Bei unterlassener Zahlung der Maklerprovision an uns kann auch keine Auszahlung der Tippgeberprovision erfolgen. Bei mehreren Tipps zu einem Objekt, erhält nur der erste Tippgeber die Provision.</p>

  <p class="website">www.wohnraum-valdorf.de</p>
</main>
</body>
</html>
```